Business Card for TLK Field Services

Would like a large logo on one side. On the other side, logo on one side and company phone number, address, and email on the other side. I don't have a logo so please create one for us.
Updates
I don't have a logo, so please create one for us.
Target Market(s)
Land Surveying
Industry/Entity Type
Surveyor
Contact Information for Business Card
Would like a large logo on one side. On the other side, logo on one side and company phone number, address, and email on the other side
Requirements
Nice to have
- would like the initials to be incorporated with the logo

```html
<!DOCTYPE html>
<html lang="en">
<head>
<meta charset="utf-8">
<title>TLK Field Services – Business Card</title>
<link href="https://fonts.googleapis.com/css2?family=Open+Sans:wght@400;700&display=swap" rel="stylesheet">
<style>
  :root {
    --navy: #0b1f5e;
    --white: #ffffff;
    --ink: #1b1b1b;
    --backdrop: #eceae6;
  }
  * { box-sizing: border-box; margin: 0; padding: 0; }
  html, body { width: 1200px; height: 900px; overflow: hidden; }
  body {
    background: var(--backdrop);
    font-family: "Open Sans", Arial, sans-serif;
    position: relative;
  }
  .card {
    position: absolute;
    border-radius: 18px;
    overflow: hidden;
    box-shadow: 0 6px 20px rgba(0,0,0,0.15);
  }
  .card--front { left: 77px; top: 35px; width: 590px; height: 364px; background: var(--white); }
  .card--back  { left: 390px; top: 505px; width: 565px; height: 350px; background: var(--navy); }

  .band { position: absolute; left: 0; right: 0; }
  .card--front .band { top: 60px; height: 98px; background: var(--navy); }
  .card--back .band  { top: 130px; height: 96px; background: var(--white); }

  .oval { position: absolute; border-radius: 50%; }
  .card--front .oval { left: 141px; top: 42px; width: 314px; height: 134px; background: var(--white); }
  .card--back .oval  { left: 115px; top: 112px; width: 322px; height: 132px; background: var(--navy); }

  .wordmark {
    position: absolute;
    text-align: center;
    font-weight: 700;
    line-height: 1;
  }
  .card--front .wordmark { left: 141px; top: 58px; width: 314px; color: var(--navy); }
  .card--back .wordmark  { left: 115px; top: 128px; width: 322px; color: var(--white); }
  .wordmark__initials { display: block; font-size: 62px; letter-spacing: 4px; }
  .wordmark__name { display: block; font-size: 26px; margin-top: 6px; letter-spacing: 0.5px; }

  .person {
    position: absolute;
    right: 314px;
    top: 236px;
    text-align: right;
    color: var(--ink);
    font-size: 15px;
    line-height: 20px;
  }
  .person__name { font-size: 22px; color: var(--navy); line-height: 28px; }
  .person__address { margin-top: 10px; }

  .contact-list {
    position: absolute;
    left: 316px;
    top: 237px;
    list-style: none;
    font-size: 15px;
    color: var(--ink);
  }
  .contact-list li { display: flex; align-items: center; height: 24.5px; }
  .contact-list svg { width: 12px; height: 12px; margin-right: 10px; fill: var(--navy); flex: none; }
</style>
</head>
<body>

<section class="card card--front" aria-label="Business card front">
  <div class="band"></div>
  <div class="oval"></div>
  <div class="wordmark">
    <span class="wordmark__initials">TLK</span>
    <span class="wordmark__name">Field Services</span>
  </div>

  <div class="person">
    <p class="person__name">Marcus Reed</p>
    <p class="person__title">Managing Director</p>
    <p class="person__address">4820, Meridian Survey Road<br>Northfield, 246810</p>
  </div>

  <ul class="contact-list">
    <li>
      <svg viewBox="0 0 24 24" aria-hidden="true"><path d="M6.6 10.8a15.1 15.1 0 0 0 6.6 6.6l2.2-2.2c.3-.3.7-.4 1-.2 1.1.4 2.3.6 3.6.6.6 0 1 .4 1 1V20c0 .6-.4 1-1 1A17 17 0 0 1 3 4c0-.6.4-1 1-1h3.5c.6 0 1 .4 1 1 0 1.3.2 2.5.6 3.6.1.3 0 .7-.2 1z"/></svg>
      (044)-555-0142
    </li>
    <li>
      <svg viewBox="0 0 24 24" aria-hidden="true"><path d="M6 2h10v6H6zM3 9h18v13H3zm4 4v2h3v-2zm5 0v2h3v-2zm-5 4v2h3v-2zm5 0v2h3v-2z"/></svg>
      044-555-0187
    </li>
    <li>
      <svg viewBox="0 0 24 24" aria-hidden="true"><path d="M2 5h20v14H2zm2 2v.5l8 5 8-5V7l-8 5z"/></svg>
      info@tlkfield.com
    </li>
    <li>
      <svg viewBox="0 0 24 24" aria-hidden="true"><circle cx="12" cy="12" r="10"/></svg>
      www.tlkfield.com
    </li>
  </ul>
</section>

<section class="card card--back" aria-label="Business card back">
  <div class="band"></div>
  <div class="oval"></div>
  <div class="wordmark">
    <span class="wordmark__initials">TLK</span>
    <span class="wordmark__name">Field Services</span>
  </div>
</section>

</body>
</html>
```